Use responsive design to make this page look and behave awesome in any size

YOU CAN SUBMIT PSD, HOWEVER, THE WINNER MUST SUBMIT PROVIDE A SINGLE CODED PAGE PER THE LINK AND INSTRUCTIONS AT THE BOTTOM OF THIS BRIEF. While developing an internal website, we realized we are not super great at making things look awesome and responsive for phone/tablet/desktop. Thats where you come in. We want you to take this code, Fork it, and then make it look awesome and work great on any size device.

Task at hand:

This page is a simple dashboard showing how a number of stores stack up against each other and against a corporate goal.

Top: Goal title, and where the logged in person's store stands in the ranking.
Green means you are in compliance
Red means you are not in compliance

Middle: Description of goal. Words to describe what the corporate goal is, and a target number.

Bottom: Here we just want to show the top 10 and bottom 5 out of 100+ stores. if your in the top ten, you are highlighted. If your in the bottom 5, you will be highlighted there too. If you are in the middle, we would put the your store info between the top and bottom... indicating your in the middle.
Green means you they are in compliance
Red means they are not in compliance

Your Mission is not only to make this look fantastic and responsive, but to have usable code in there.

You don't need to do any logic. All we care about is look and feel and responsive behavior on different size browsers.

The winner obviously gets the prize, and hopefully can become a solid resource to do more of this type of thing for us in the future.

Instructions:
Go to this link: https://codequill.example/edit/tvx-leaderpanel-widget
Click on the blue Fork button. This will give you a new URL that you can paste back into the contest to review results for us to see your work.
Uploading pictures is not necessary as the responsive code is what is important here.

Good luck!

Number of Pages Required

1 page

Requirements
Must have
• The page must be responsive and look very professional AND game like.
Should not have
• plugins. just native code

```html
<!DOCTYPE html>
<html lang="en">
<head>
<meta charset="utf-8">
<title>Lead Measures</title>
<link rel="stylesheet" href="https://fonts.googleapis.com/css2?family=Open+Sans:wght@400;600;700&display=swap">
<style>
  :root {
    --brand-blue: #03b0ea;
    --panel-head: #47555f;
    --ok-green: #3cc83c;
    --ok-text: #45b94a;
    --bad-text: #e0303d;
    --highlight: #dc3545;
    --ink: #222;
    --rule: #e6e6e6;
    --page: #ffffff;
    --column-bg: #ffffff;
  }
  * { box-sizing: border-box; margin: 0; padding: 0; }
  html, body { width: 1131px; height: 1200px; overflow: hidden; background: var(--page); }
  body { font-family: "Open Sans", Arial, sans-serif; color: var(--ink); }
  .dashboard { width: 1131px; height: 1200px; padding-top: 24px; }
  .dashboard-title {
    background: var(--brand-blue); color: #fff; text-align: center;
    font-size: 26px; font-weight: 600; height: 76px; line-height: 76px;
    margin: 0 24px;
  }
  .measures {
    display: grid; grid-template-columns: repeat(4, 1fr); gap: 26px;
    margin: 18px 24px 0;
  }
  .measure { background: var(--column-bg); box-shadow: 0 0 0 1px var(--rule); }
  .measure-head {
    background: var(--panel-head); color: #fff; height: 60px;
    display: flex; align-items: center; justify-content: center; gap: 20px;
    font-size: 19px; font-weight: 700;
  }
  .measure-score { color: var(--ok-green); font-weight: 600; }
  .measure-goal {
    display: flex; justify-content: space-between; align-items: flex-start;
    padding: 20px 24px 0 10px; height: 90px; border-bottom: 1px solid var(--rule);
  }
  .goal-text { font-size: 11.5px; line-height: 1.15; max-width: 180px; }
  .goal-target { font-size: 20px; white-space: nowrap; }
  .rankings { width: 100%; border-collapse: collapse; font-size: 12px; }
  .rankings td { height: 42px; border-bottom: 1px solid var(--rule); }
  .rankings .rank { width: 50px; text-align: center; font-weight: 700; }
  .rankings .store { text-align: center; }
  .rankings .value { width: 60px; text-align: right; padding-right: 20px; }
  .rankings tr.ok .store, .rankings tr.ok .value { color: var(--ok-text); }
  .rankings tr.bad .store, .rankings tr.bad .value { color: var(--bad-text); }
  .rankings tr.mine td { background: var(--highlight); color: #fff; }
  .rankings tr.mine .rank { font-weight: 400; }
  .rankings tr.mine .store { font-weight: 600; }
  .rankings tr.gap td { height: 24px; border-bottom: 1px solid var(--rule); }
</style>
</head>
<body>
<main class="dashboard">
  <h1 class="dashboard-title">Lead Measures</h1>
  <section class="measures">

    <article class="measure">
      <header class="measure-head"><span>Team</span><span class="measure-score">92.1%</span></header>
      <div class="measure-goal"><p class="goal-text">Use Slow Stock wherever possible</p><p class="goal-target">80%</p></div>
      <table class="rankings">
        <tr class="bad"><td class="rank">1</td><td class="store">(1) yjcQbtCyQu</td><td class="value">1%</td></tr>
        <tr class="bad"><td class="rank">2</td><td class="store">(1) crsmicfXwS</td><td class="value">1%</td></tr>
        <tr class="bad"><td class="rank">3</td><td class="store">(2) wnLJojLRSf</td><td class="value">2%</td></tr>
        <tr class="bad"><td class="rank">4</td><td class="store">(2) swEbjeRrpi</td><td class="value">2%</td></tr>
        <tr class="bad"><td class="rank">5</td><td class="store">(4) oUauMPncOA</td><td class="value">4%</td></tr>
        <tr class="bad"><td class="rank">6</td><td class="store">(5) vYuFdHZExR</td><td class="value">5%</td></tr>
        <tr class="bad"><td class="rank">7</td><td class="store">(5) jvBnNaGkeE</td><td class="value">5%</td></tr>
        <tr class="bad"><td class="rank">8</td><td class="store">(6) CuWIlvexCs</td><td class="value">6%</td></tr>
        <tr class="bad"><td class="rank">9</td><td class="store">(7) XQFCUbSoko</td><td class="value">7%</td></tr>
        <tr class="bad"><td class="rank">10</td><td class="store">(7) GucpFDVVJP</td><td class="value">7%</td></tr>
        <tr class="gap"><td colspan="3"></td></tr>
        <tr class="ok"><td class="rank">96</td><td class="store">(94) VaDGNkvwai</td><td class="value">94%</td></tr>
        <tr class="ok"><td class="rank">97</td><td class="store">(94) IBjPTiBSIh</td><td class="value">94%</td></tr>
        <tr class="ok"><td class="rank">98</td><td class="store">(96) iWwFhTvkZb</td><td class="value">96%</td></tr>
      </table>
    </article>

    <article class="measure">
      <header class="measure-head"><span>Slow</span><span class="measure-score">0%</span></header>
      <div class="measure-goal"><p class="goal-text">Less than 0% of inventory slower than 100 days</p><p class="goal-target">&lt; 1%</p></div>
      <table class="rankings">
        <tr class="ok"><td class="rank">1</td><td class="store">(89) NZBGVuImnc</td><td class="value">0%</td></tr>
        <tr class="ok"><td class="rank">2</td><td class="store">(80) GaccDehKUO</td><td class="value">0%</td></tr>
        <tr class="ok"><td class="rank">3</td><td class="store">(55) aPfpNcqcDh</td><td class="value">0%</td></tr>
        <tr class="ok"><td class="rank">4</td><td class="store">(97) YqyVfKITll</td><td class="value">0%</td></tr>
        <tr class="ok"><td class="rank">5</td><td class="store">(67) PvQdqyeaHr</td><td class="value">0%</td></tr>
        <tr class="mine"><td class="rank">6</td><td class="store">(00) Your Store</td><td class="value">2%</td></tr>
        <tr class="bad"><td class="rank">7</td><td class="store">(40) jyMfVYIVbl</td><td class="value">2%</td></tr>
        <tr class="bad"><td class="rank">8</td><td class="store">(11) QSESmpDJqw</td><td class="value">2%</td></tr>
        <tr class="bad"><td class="rank">9</td><td class="store">(71) nIIaXFpJWv</td><td class="value">2%</td></tr>
        <tr class="bad"><td class="rank">10</td><td class="store">(51) ENrkkveKpb</td><td class="value">2%</td></tr>
        <tr class="gap"><td colspan="3"></td></tr>
        <tr class="bad"><td class="rank">96</td><td class="store">(90) VZgTUWgJTU</td><td class="value">8%</td></tr>
        <tr class="bad"><td class="rank">97</td><td class="store">(67) nRGVsKcZhP</td><td class="value">9%</td></tr>
        <tr class="bad"><td class="rank">98</td><td class="store">(32) JckeFPUVJV</td><td class="value">9%</td></tr>
      </table>
    </article>

    <article class="measure">
      <header class="measure-head"><span>Turns</span><span class="measure-score">2.2</span></header>
      <div class="measure-goal"><p class="goal-text">Turn inventory 6 or more times a year</p><p class="goal-target">&gt; 6</p></div>
      <table class="rankings">
        <tr class="bad"><td class="rank">1</td><td class="store">(8) VZaEOSVkef</td><td class="value">0.2</td></tr>
        <tr class="bad"><td class="rank">2</td><td class="store">(3) PcVKNpUNmj</td><td class="value">0.2</td></tr>
        <tr class="bad"><td class="rank">3</td><td class="store">(4) RIlyRZsTIn</td><td class="value">0.4</td></tr>
        <tr class="bad"><td class="rank">4</td><td class="store">(9) epiNQFtERO</td><td class="value">0.6</td></tr>
        <tr class="bad"><td class="rank">5</td><td class="store">(3) FbFOzkjSpF</td><td class="value">0.7</td></tr>
        <tr class="bad"><td class="rank">6</td><td class="store">(7) RdzzkcVqtC</td><td class="value">0.8</td></tr>
        <tr class="bad"><td class="rank">7</td><td class="store">(1) DiilXiGkTx</td><td class="value">0.8</td></tr>
        <tr class="bad"><td class="rank">8</td><td class="store">(1) jxWbwORyVa</td><td class="value">0.8</td></tr>
        <tr class="bad"><td class="rank">9</td><td class="store">(4) UyzYfilMzU</td><td class="value">0.8</td></tr>
        <tr class="bad"><td class="rank">10</td><td class="store">(4) KVIgJQBgAc</td><td class="value">1</td></tr>
        <tr class="gap"><td colspan="3"></td></tr>
        <tr class="ok"><td class="rank">96</td><td class="store">(5) gBeGhPqZNF</td><td class="value">9.7</td></tr>
        <tr class="ok"><td class="rank">97</td><td class="store">(8) gGhhZFICHP</td><td class="value">9.7</td></tr>
        <tr class="ok"><td class="rank">98</td><td class="store">(9) emavLKfhzN</td><td class="value">9.8</td></tr>
      </table>
    </article>

    <article class="measure">
      <header class="measure-head"><span>Values</span><span class="measure-score">1.9</span></header>
      <div class="measure-goal"><p class="goal-text">Inventory Value to be around 1.25 x you last months INVENTORY sales</p><p class="goal-target">1.25</p></div>
      <table class="rankings">
        <tr class="ok"><td class="rank">1</td><td class="store">(8) VZaEOSVkef</td><td class="value">0.2</td></tr>
        <tr class="ok"><td class="rank">2</td><td class="store">(3) PcVKNpUNmj</td><td class="value">0.2</td></tr>
        <tr class="ok"><td class="rank">3</td><td class="store">(4) RIlyRZsTIn</td><td class="value">0.4</td></tr>
        <tr class="ok"><td class="rank">4</td><td class="store">(9) epiNQFtERO</td><td class="value">0.6</td></tr>
        <tr class="ok"><td class="rank">5</td><td class="store">(3) FbFOzkjSpF</td><td class="value">0.7</td></tr>
        <tr class="ok"><td class="rank">6</td><td class="store">(7) RdzzkcVqtC</td><td class="value">0.8</td></tr>
        <tr class="ok"><td class="rank">7</td><td class="store">(1) DiilXiGkTx</td><td class="value">0.8</td></tr>
        <tr class="ok"><td class="rank">8</td><td class="store">(1) jxWbwORyVa</td><td class="value">0.8</td></tr>
        <tr class="ok"><td class="rank">9</td><td class="store">(4) UyzYfilMzU</td><td class="value">0.8</td></tr>
        <tr class="ok"><td class="rank">10</td><td class="store">(7) SCXuIMdjcB</td><td class="value">1</td></tr>
        <tr class="gap"><td colspan="3"></td></tr>
        <tr class="bad"><td class="rank">96</td><td class="store">(5) gBeGhPqZNF</td><td class="value">9.7</td></tr>
        <tr class="bad"><td class="rank">97</td><td class="store">(8) gGhhZFICHP</td><td class="value">9.7</td></tr>
        <tr class="bad"><td class="rank">98</td><td class="store">(9) emavLKfhzN</td><td class="value">9.8</td></tr>
      </table>
    </article>

  </section>
</main>
</body>
</html>
```